電子書籍の表紙を作成お願い致します。

50歳以上の更年期女性が対象のダイエット本です。
更年期をむかえてから、ソウルメロディダイエットで7キロ痩せることに成功した体験が書かれています。

たくさんあるダイエット本に埋もれないような、
ダイエットという言葉に反応する、美意識の高い更年期女性の目につく、明るく楽し気なデザインを期待しています。

その他、何か不明な点等ございましたら、お気軽におtぴ合わせください。

宜しくお願い致します。

著者顔写真と原稿を追記します。
参考にしてください。
著者の肩書は、
ダイエットアドバイザー フィットネスインストラクター
とよろしくお願いいたします。
募集締め切りがいよいよ16時間をきりました。
すでに、いくつかの素敵なデザインをいただいていますが、
最後の逆転大ホームランを狙っている、あなたの応募を心よりお待ちしています。

選んだ理由としては、
①美意識高い女性が好むピンクがメインのデザイン
②ソウルメロディダイエットもタイトルが一番見やすい
③ビフォーアフターのイラストが可愛い
などです。

この度は、たくさんの素敵なデザインを提案いただき、本当にありがとうございました。
初めての電子書籍で大変でしたが、デザイナーの皆さんのおかげで、毎日ワクワクして、
この表紙選定が一番楽しい作業になりました。

今回残念ながら、次点になった2点もとても評判が良いものでした。
そのほかのデザインも、とても個性的で素敵でした。
本当にありがとうございました。

次回お世話になる際には、またよろしくお願いいたします。

```html
<!DOCTYPE html>
<html lang="ja">
<head>
<meta charset="utf-8">
<title>50歳からのソウルメロディダイエット</title>
<link rel="stylesheet" href="https://fonts.googleapis.com/css2?family=Noto+Sans+JP:wght@500;700;900&family=M+PLUS+Rounded+1c:wght@700;800;900&display=swap">
<style>
:root{
  --paper:#ffffff;
  --ink:#1d1d1f;
  --navy:#2b3350;
  --red:#e8342c;
  --pink:#e6177e;
  --yellow:#ffe93a;
  --yellow-deep:#ffd400;
  --green:#a9d67b;
  --illus-a:#fde6ee;
  --illus-b:#e3f2d3;
}
*{margin:0;padding:0;box-sizing:border-box}
html,body{width:752px;height:1200px;overflow:hidden;background:var(--paper)}
.cover{position:relative;width:752px;height:1200px;background:var(--paper);overflow:hidden;font-family:"Noto Sans JP",sans-serif;color:var(--ink)}
.cover p,.cover span,.cover div{white-space:nowrap}
.burst{position:absolute;left:0;top:0;width:400px;height:360px}
.catch-num{position:absolute;left:36px;top:18px;font-family:"M PLUS Rounded 1c",sans-serif;font-weight:900;font-size:190px;line-height:1;color:var(--red)}
.catch-badge{position:absolute;left:150px;top:10px;width:104px;height:104px;border-radius:50%;background:var(--red);color:#fff;display:flex;align-items:center;justify-content:center;text-align:center;font-family:"M PLUS Rounded 1c",sans-serif;font-weight:900;font-size:25px;line-height:1.15}
.catch-unit{position:absolute;left:132px;top:118px;font-family:"M PLUS Rounded 1c",sans-serif;font-weight:900;font-size:54px;color:var(--red);line-height:1}
.catch-result{position:absolute;left:136px;top:204px;font-weight:900;font-size:40px;line-height:1;color:var(--ink)}
.illustration{position:absolute;left:392px;top:0;width:320px;height:312px;background:radial-gradient(ellipse at 50% 55%,var(--illus-a) 0%,#fbd7e3 45%,var(--illus-b) 100%)}
.lead{position:absolute;left:96px;top:316px;font-weight:900;font-size:40px;line-height:1.2;color:var(--navy)}
.lead::before{content:"＼";margin-right:4px}
.lead::after{content:"／";margin-left:4px}
.title-age{position:absolute;left:96px;top:378px;font-weight:900;font-size:86px;line-height:1;color:var(--ink)}
.title-age small{font-size:74px}
.title-main{position:absolute;left:100px;top:482px;font-weight:900;font-size:80px;line-height:1;color:var(--pink);letter-spacing:2px}
.title-sub{position:absolute;left:120px;top:578px;font-weight:900;font-size:104px;line-height:1;color:var(--pink);letter-spacing:2px}
.gift-tag{position:absolute;left:80px;top:808px;width:196px;height:100px;background:var(--yellow-deep);transform:rotate(-8deg);display:flex;align-items:center;justify-content:center;text-align:center;font-family:"M PLUS Rounded 1c",sans-serif;font-weight:900;font-size:28px;line-height:1.25;color:var(--red);border-radius:6px}
.author-role{position:absolute;left:360px;top:796px;font-weight:700;font-size:21px;line-height:1.4;color:var(--ink)}
.author-name{position:absolute;left:360px;top:854px;font-weight:700;font-size:44px;line-height:1.1;letter-spacing:3px;color:var(--ink)}
.bonus-band{position:absolute;left:0;top:934px;width:752px;height:182px;background:var(--green);display:flex;flex-direction:column;justify-content:center;align-items:center;font-weight:900;font-size:42px;line-height:1.35;color:var(--navy)}
.bonus-band .accent{color:var(--red);font-size:60px;line-height:1}
</style>
</head>
<body>
<main class="cover">
  <svg class="burst" viewBox="0 0 400 360" aria-hidden="true">
    <polygon fill="var(--yellow)" points="390,150 345,180 370,228 318,240 322,292 270,288 252,336 205,312 170,352 135,312 88,336 70,288 18,292 22,240 -30,228 -5,180 -50,150 -5,120 -30,72 22,60 18,8 70,12 88,-36 135,-12 170,-52 205,-12 252,-36 270,12 322,8 318,60 370,72 345,120"/>
  </svg>
  <div class="catch-num">7</div>
  <div class="catch-badge">更年期<br>でも</div>
  <div class="catch-unit">キロ</div>
  <div class="catch-result">痩せられた！</div>

  <div class="illustration" role="img" aria-label="体重計に乗って喜ぶ女性のイラスト"></div>

  <p class="lead">これが最後！</p>
  <h1>
    <span class="title-age">50歳<small>からの</small></span>
    <span class="title-main">ソウルメロディ</span>
    <span class="title-sub">ダイエット</span>
  </h1>

  <div class="gift-tag">読者限定<br>プレゼント！</div>
  <p class="author-role">ダイエットアドバイザー<br>フィットネスインストラクター</p>
  <p class="author-name">森川さやこ</p>

  <div class="bonus-band">
    <span>家事の合間の<span class="accent">3</span>分で出来る、</span>
    <span>おなか引き締め動画</span>
  </div>
</main>
</body>
</html>
```